Brightbay Business Card Design

Our company is called Brightbay. We manufacture confectionary snacks & frozen novelties. Our initial product portfolio includes frozen ice lollies/popsicles & stick ice cream bars.

We require a business card design.

Please use the attached Logo.

Please use an orange, brown, yellow colour code. You may choose any combination of the 3 or include all three. The logo however must remain orange.

Target Market(s)

Business card will be targeted at distributors of our products such as supermarket procurement managers, convenience store owners, wholesale distributors and merchandising agents.

Industry/Entity Type

Business

Requirements
Must have
• Calvin Obeng_Director/ P.O.Box Dunmore 5172, Accra, Ghana / m: 00233(0)507318924/ e: calvin.obeng@mailvora.co.uk

```html
<!DOCTYPE html>
<html lang="en">
<head>
<meta charset="utf-8">
<title>Brightbay Business Card</title>
<link rel="stylesheet" href="https://fonts.googleapis.com/css2?family=Arvo:wght@400;700&display=swap">
<style>
  :root {
    --backdrop: #d9d9d9;
    --card-brown: #5e3714;
    --brand-orange: #ee6b1f;
    --accent-yellow: #f6c72a;
    --paper-white: #fafafa;
    --text-light: #ffffff;
  }
  * { margin: 0; padding: 0; box-sizing: border-box; }
  html, body {
    width: 1200px;
    height: 900px;
    overflow: hidden;
    background: var(--backdrop);
  }
  .business-card {
    position: absolute;
    left: 150px;
    top: 193px;
    width: 900px;
    height: 514px;
    background: var(--card-brown);
    overflow: hidden;
    font-family: "Arvo", Georgia, serif;
    color: var(--text-light);
    box-shadow: 0 14px 30px rgba(0, 0, 0, 0.18);
  }
  .card-arcs {
    position: absolute;
    inset: 0;
  }
  .brand-name {
    position: absolute;
    left: 70px;
    top: 148px;
    font-weight: 700;
    font-size: 66px;
    letter-spacing: -1px;
    color: var(--brand-orange);
    line-height: 1.2;
  }
  .contact-block {
    position: absolute;
    right: 44px;
    top: 272px;
    text-align: right;
  }
  .person-name {
    font-weight: 700;
    font-size: 35px;
    line-height: 1.1;
  }
  .person-role {
    font-weight: 400;
    font-size: 28px;
    line-height: 1.2;
  }
  .postal-address {
    margin-top: 30px;
    font-size: 23px;
    line-height: 1.3;
  }
  .phone-email {
    margin-top: 6px;
    font-size: 23px;
    line-height: 1.3;
  }
</style>
</head>
<body>
  <section class="business-card">
    <svg class="card-arcs" width="900" height="514" viewBox="0 0 900 514" aria-hidden="true">
      <ellipse cx="60" cy="77" rx="562" ry="278" fill="var(--brand-orange)"/>
      <ellipse cx="60" cy="77" rx="548" ry="264" fill="var(--accent-yellow)"/>
      <ellipse cx="60" cy="77" rx="534" ry="250" fill="var(--paper-white)"/>
    </svg>
    <div class="brand-name">Brightbay</div>
    <div class="contact-block">
      <p class="person-name">Calvin Obeng</p>
      <p class="person-role">Director</p>
      <p class="postal-address">P.O.Box Dunmore 5172, Accra, Ghana</p>
      <p class="phone-email">m: 00233(0)507318924 &nbsp;|&nbsp; e: calvin.obeng@mailvora.co.uk</p>
    </div>
  </section>
</body>
</html>
```